Discreet simple classy for adult entertainment

I would like a matte black business card with gold writing for my business. Keeping it simple. Having my following:

Lina frost
Events. Entertainment. Promotions
0477250618

or alternatively could have what i had on my previous card below but i think i prefer the above as again - discretion.

Maybe a nice gold line thru the card or some other very simple design . Or not open to ideas/ can be doublesided if any good ideas with that.

included pics of my old bus card. not sure weather i want a photo on it or not. if i do it wont be the same pic. i kinda wanted a card that was discreet so if it was in someones wallet they wouldn't neccessarily realise it was from a stripper.

Target Market(s)

men

Industry/Entity Type

Business

Contact Information for Business Card

Lina frost
0477250618

Requirements
Nice to have
• i don't know i am really open to anything. im giving my cards to guys so something they can have in their wallet that is discreet preferably.

```html
<!DOCTYPE html>
<html lang="en">
<head>
<meta charset="utf-8">
<title>Lina Frost — Business Card</title>
<link rel="stylesheet" href="https://fonts.googleapis.com/css2?family=Jost:wght@300;400&display=swap">
<style>
  :root {
    --page-bg: #ecf0cf;
    --card-dark: #0c0c0c;
    --card-light: #3a3a3a;
    --gold: #b08a4e;
    --text-light: #c9c9c9;
  }
  html, body {
    margin: 0;
    padding: 0;
    width: 1200px;
    height: 1000px;
    overflow: hidden;
    background: var(--page-bg);
  }
  .canvas {
    position: relative;
    width: 1200px;
    height: 1000px;
  }
  .business-card {
    position: absolute;
    left: 180px;
    top: 260px;
    width: 840px;
    height: 480px;
    background: linear-gradient(100deg, var(--card-light) 0%, #222 50%, var(--card-dark) 100%);
    font-family: "Jost", "Helvetica Neue", Arial, sans-serif;
  }
  .card-frame {
    position: absolute;
    inset: 0;
  }
  .card-identity {
    position: absolute;
    left: 0;
    right: 0;
    top: 200px;
    text-align: center;
  }
  .card-name {
    margin: 0;
    color: var(--gold);
    font-weight: 300;
    font-size: 38px;
    letter-spacing: 0.06em;
    text-transform: uppercase;
    line-height: 1;
  }
  .card-phone {
    margin: 14px 0 0;
    color: var(--text-light);
    font-weight: 300;
    font-size: 24px;
    letter-spacing: 0.02em;
    line-height: 1;
  }
  .card-tagline {
    position: absolute;
    right: 94px;
    bottom: 28px;
    margin: 0;
    color: var(--text-light);
    font-weight: 300;
    font-size: 21px;
    letter-spacing: 0.03em;
    line-height: 1;
    white-space: nowrap;
  }
</style>
</head>
<body>
  <main class="canvas">
    <section class="business-card" aria-label="Lina Frost business card">
      <svg class="card-frame" width="840" height="480" viewBox="0 0 840 480" aria-hidden="true">
        <g fill="none" stroke="var(--gold)" stroke-width="1.5">
          <polyline points="412,440 40,440 40,40 800,40 800,440 758,440"/>
        </g>
      </svg>
      <div class="card-identity">
        <h1 class="card-name">Lina Frost</h1>
        <p class="card-phone">0477250618</p>
      </div>
      <p class="card-tagline">Events. Entertainment. Promotions.</p>
    </section>
  </main>
</body>
</html>
```